Home Page Design for Motor Manufacturer

Hello,
please design the homepage for a manufacturer of industry motors. I am looking for a professional, clean and minimalistic design. Since this a rather conservative industry it should get a professional look but since it is a redesign there should be some modern that gives is the modern touch of innovation.
A competitor's homepage I like is:
https://www.valtrosk.com/en/
What I like about this website:
* clean, minimal, well structured design
* mega menu
For this project please find attached the wireframes (most buttons are in German but by context and Google translate you will easily figure it out; only unclear - "Messe" means "trade exhibition"). The paddings and margins are NOT exact. Also any color of backgrounds etc. chosen is not meant to represent a real color but rather to illustrate the object and maybe show there should be some background emphasis (color or image).
Wireframes:
https: //www.filmavek. com / t / pxuTQmD7ZJHaLrwY
In both wireframes the only thing that is different is the Service section. I expect from the winner both designs for this service section: one with normal cart design and one with tabs as filters to search products (find image for product categories attached)
In the header use on the left the following text:
h1: "Your competent partner for industrial engines,
-transmission and drawing parts
with more than 5000 satisfied customers "
primary button: Our products
sec. button: Download catalog
and on the right side we feature one or more product images (like putting them in a nice display together).
I also think of a solid background color or subtle gradient for the hero section.
The winner should also design an open mega menu version.
Menu items in this order:
• Home page
• Gearboxes & Motors
• Engine components
• Drawing parts
• Machines & accessories
• About us
• Contact
Also create a language switch with globe symbol and DE for Germany and EN for English above the nav plus the telephone number with icon (user dummy number +49 (0) 987654321)
Output should be in Figma, Sketch or PSD.
Fonts + color to use:
header: Proza Libre, bold, # 0171A1
body: Open Sans, regular, black
Primary accent color: # 0171A1
Text black or dark gray
background: light gray, white or shade of blue
More image resources:
https://www.filmavek.com/t/QrnLVdHZPKEX1bmu
If there are any questions please do not hesitate to ask.
Target Market(s)
B2B - anyone with industrial machinery needing small motors (not car engines)
Industry/Entity Type
Manufacturing
Number of Pages Required
1 page
Requirements
Must have
- see above
Nice to have
- see above
Should not have
- see above

```html
<!DOCTYPE html>
<html lang="en">
<head>
<meta charset="utf-8">
<title>KVR GmbH – Industrial Motors</title>
<link rel="stylesheet" href="https://fonts.googleapis.com/css2?family=Proza+Libre:wght@400;600;700&family=Open+Sans:ital,wght@0,400;0,600;0,700;1,400&display=swap">
<style>
:root{
  --accent:#0171a1;
  --accent-dark:#045d86;
  --navy:#063f66;
  --sky:#3db5e0;
  --cyan:#159fcf;
  --ink:#1c1c1c;
  --text:#555;
  --muted:#8a8a8a;
  --line:#e4e4e4;
  --bg-soft:#f6f6f6;
  --white:#fff;
}
*{box-sizing:border-box;margin:0;padding:0}
html,body{width:1200px;height:5080px;overflow:hidden;background:var(--white)}
body{font-family:"Open Sans",sans-serif;color:var(--ink);position:relative}
.abs{position:absolute}
h2.section-title{position:absolute;left:0;width:1200px;text-align:center;font-family:"Proza Libre",sans-serif;font-weight:600;font-size:27px;letter-spacing:.5px;color:#222}
.btn{position:absolute;display:flex;align-items:center;justify-content:center;font-size:10px;font-weight:700;letter-spacing:.5px;text-transform:uppercase}
.btn-primary{background:var(--accent);color:var(--white)}
.btn-outline{border:2px solid var(--accent);color:var(--accent);background:var(--white)}
p.body{font-size:11px;line-height:22.7px;color:var(--text)}

.top-stripe{left:0;top:0;width:1200px;height:10px;background:var(--accent)}
.brand{left:162px;top:24px;display:flex;align-items:center;gap:8px;font-family:"Proza Libre",sans-serif;font-weight:700;font-size:34px;color:var(--accent);letter-spacing:1px}
.brand .mark{width:14px;height:14px;background:var(--accent)}
.search{left:407px;top:26px;width:313px;height:30px;border:1px solid var(--line);border-radius:3px;font-size:9px;color:#aaa;padding:0 10px;display:flex;align-items:center;justify-content:space-between}
.phone{left:866px;top:33px;font-size:10px;color:var(--accent);display:flex;align-items:center;gap:6px}
.lang{left:995px;top:33px;font-size:10px;color:var(--accent);display:flex;align-items:center;gap:5px}
.nav{left:0;top:72px;width:1200px;height:60px;border-top:1px solid var(--line);border-bottom:1px solid var(--line)}
.nav a{position:absolute;top:22px;font-size:11px;color:#333;text-decoration:none;letter-spacing:.3px}

.hero{left:0;top:132px;width:1200px;height:698px;background:linear-gradient(115deg,#e7e7e7 0%,#f1f1f1 40%,#fbfbfb 75%,#fff 100%)}
.hero .eyebrow{left:160px;top:186px;font-size:10px;letter-spacing:2px;color:var(--accent)}
.hero h1{left:160px;top:206px;width:480px;font-family:"Proza Libre",sans-serif;font-weight:700;font-size:26px;line-height:37.5px;color:var(--accent);white-space:nowrap}
.hero h1 u{text-decoration-thickness:2px;text-underline-offset:4px}
.hero-media{left:690px;top:134px;width:440px;height:336px;border-radius:12px;background:radial-gradient(ellipse at 55% 50%,#d9dfe4 0%,#e9ecef 55%,rgba(240,240,240,0) 75%)}
.dots{left:573px;top:596px;display:flex;align-items:center;gap:8px}
.dots span{width:9px;height:9px;border-radius:50%;background:#b9d3e0}
.dots span.on{width:16px;height:16px;background:var(--white);border:3px solid var(--accent)}

.advantages{left:160px;top:770px;width:880px;height:225px;display:flex}
.advantage{flex:1;color:var(--white);text-align:center;padding-top:44px}
.advantage svg{display:block;margin:0 auto 12px}
.advantage h3{font-size:12px;font-weight:700;margin-bottom:10px}
.advantage p{font-size:10px;line-height:22px;padding:0 48px}

.card{position:absolute;width:418px;height:418px;border:1px solid var(--line);background:var(--white)}
.card .shot{position:absolute;left:90px;top:70px;width:238px;height:210px;border-radius:8px;background:radial-gradient(ellipse at center,#dfe6ec 0%,#eef2f5 55%,#fff 80%)}
.card h3{position:absolute;left:0;top:308px;width:100%;text-align:center;font-size:13px;font-weight:400;color:#222}
.card-btn{width:140px;height:45px}

.fairs{left:0;top:2270px;width:1200px;height:1175px;background:var(--bg-soft);border-top:1px solid var(--line);border-bottom:1px solid var(--line)}
.fair-img{position:absolute;left:162px;width:352px;height:270px;background:linear-gradient(135deg,#3f7fb9 0%,#5b9fd6 45%,#8bc0e6 100%)}
.fair-body{position:absolute;left:559px;width:467px}
.fair-body h3{font-size:14px;font-weight:600;color:#222;margin-bottom:12px}

.about-img{position:absolute}
.feature-list{list-style:none}
.feature-list li{font-size:11px;font-weight:600;color:var(--accent);line-height:26.5px;display:flex;align-items:center;gap:9px}
.feature-list li::before{content:"";width:5px;height:5px;border-radius:50%;background:var(--accent)}
.learn{font-size:10px;font-weight:700;color:var(--accent);letter-spacing:.5px;display:flex;align-items:center;gap:8px}

.downloads{left:0;top:4001px;width:1200px;height:549px;background:var(--bg-soft);border-top:1px solid var(--line)}
.dl-img{left:162px;top:154px;width:335px;height:322px;background:linear-gradient(140deg,#cfd3d6 0%,#b4b9bd 50%,#dadcde 100%)}
.dl-panel{left:497px;top:154px;width:539px;height:322px;background:var(--white);border:1px solid var(--line)}

.contact{left:0;top:4550px;width:1200px;height:192px;background:linear-gradient(180deg,#fff 0%,#fbfcfd 100%)}
.contact .label{font-size:10px;color:#555}
.contact .value{font-size:12.5px;font-weight:700;color:#222;margin-top:6px}

.footer{left:0;top:4742px;width:1200px;height:338px;background:var(--accent);color:var(--white)}
.footer h4{position:absolute;top:56px;font-family:"Proza Libre",sans-serif;font-weight:600;font-size:18px}
.footer ul{position:absolute;top:110px;list-style:none}
.footer li{font-size:10px;line-height:23.6px}
.footer p{font-size:10px;line-height:22px}
.news-input{left:835px;top:168px;width:165px;height:38px;background:#1a86b3;font-size:9px;padding:0 14px;display:flex;align-items:center;color:#d5eaf3}
.news-send{left:1000px;top:168px;width:38px;height:38px;background:var(--white);display:flex;align-items:center;justify-content:center}
.bottom-line{top:276px;font-size:10px}
.social{display:inline-block;width:10px;height:10px;border-radius:50%;background:var(--white);margin-left:8px;vertical-align:middle}
</style>
</head>
<body>

<div class="abs top-stripe"></div>
<div class="abs brand"><span>KVR</span><span class="mark"></span></div>
<div class="abs search"><span>Make your search here...</span>
  <svg width="11" height="11" viewBox="0 0 12 12"><circle cx="5" cy="5" r="3.8" fill="none" stroke="#bbb" stroke-width="1.3"/><line x1="8" y1="8" x2="11" y2="11" stroke="#bbb" stroke-width="1.3"/></svg></div>
<div class="abs phone">
  <svg width="11" height="11" viewBox="0 0 24 24"><path fill="#0171a1" d="M6.6 10.8a15 15 0 006.6 6.6l2.2-2.2c.3-.3.7-.4 1-.2 1.1.4 2.3.6 3.6.6.6 0 1 .4 1 1V20c0 .6-.4 1-1 1A17 17 0 013 4c0-.6.4-1 1-1h3.5c.6 0 1 .4 1 1 0 1.3.2 2.5.6 3.6.1.3 0 .7-.2 1z"/></svg>
  <span>+49 (0) 987654321</span></div>
<div class="abs lang">
  <svg width="11" height="11" viewBox="0 0 24 24" fill="none" stroke="#0171a1" stroke-width="2"><circle cx="12" cy="12" r="10"/><path d="M2 12h20M12 2c3 3 3 17 0 20M12 2c-3 3-3 17 0 20"/></svg>
  <span>DE</span>
  <svg width="7" height="5" viewBox="0 0 8 5"><path d="M0 0h8L4 5z" fill="#0171a1"/></svg></div>

<nav class="abs nav">
  <a style="left:162px">HOME</a>
  <a style="left:235px">GEARBOX &amp; MOTORS</a>
  <a style="left:393px">ENGINE COMPONENTS</a>
  <a style="left:561px">DRAWING PARTS</a>
  <a style="left:693px">MACHINES &amp; ACCESSORIES</a>
  <a style="left:884px">ABOUT US</a>
  <a style="left:981px">CONTACT</a>
</nav>

<section class="abs hero">
  <div class="abs eyebrow">WELCOME TO KVR GMBH</div>
  <h1 class="abs">Your competent partner for the<br>industrial engines - transmission<br>and drawing parts with more than<br><u>5000</u> satisfied costumers!</h1>
  <div class="btn btn-primary" style="left:160px;top:395px;width:140px;height:43px">Our products</div>
  <div class="btn btn-outline" style="left:310px;top:395px;width:176px;height:43px">Download catalog</div>
  <div class="abs hero-media" role="img" aria-label="Product display: cycloidal gearbox, right-angle gearbox and planetary gear motor"></div>
  <div class="abs dots"><span></span><span class="on"></span><span></span></div>
</section>

<div class="abs advantages">
  <div class="advantage" style="background:var(--sky)">
    <svg width="26" height="26" viewBox="0 0 24 24" fill="none" stroke="#fff" stroke-width="1.5"><rect x="5" y="3" width="14" height="18" rx="1"/><path d="M8 8h8M8 12h8M8 16h5"/></svg>
    <h3>Vorteil 1</h3><p>Lorem Ipsum is simply dummy text of the printing and typesetting industry.</p></div>
  <div class="advantage" style="background:var(--cyan)">
    <svg width="26" height="26" viewBox="0 0 24 24" fill="none" stroke="#fff" stroke-width="1.5"><circle cx="12" cy="12" r="9"/><circle cx="12" cy="12" r="5"/><circle cx="12" cy="12" r="1.5"/></svg>
    <h3>Vorteil 2</h3><p>Lorem Ipsum is simply dummy text of the printing and typesetting industry.</p></div>
  <div class="advantage" style="background:#0b78ae">
    <svg width="26" height="26" viewBox="0 0 24 24" fill="none" stroke="#fff" stroke-width="1.5"><circle cx="12" cy="12" r="3"/><path d="M12 2v3M12 19v3M2 12h3M19 12h3M5 5l2 2M17 17l2 2M5 19l2-2M17 7l2-2"/></svg>
    <h3>Vorteil 3</h3><p>Lorem Ipsum is simply dummy text of the printing and typesetting industry.</p></div>
  <div class="advantage" style="background:var(--navy)">
    <svg width="26" height="26" viewBox="0 0 24 24" fill="none" stroke="#fff" stroke-width="1.5"><rect x="6" y="7" width="12" height="10"/><path d="M2 12h4M18 12h4M9 7V4M15 7V4"/></svg>
    <h3>Vorteil 4</h3><p>Lorem Ipsum is simply dummy text of the printing and typesetting industry.</p></div>
</div>

<h2 class="section-title" style="top:1064px">PRODUKTE</h2>
<div class="card" style="left:162px;top:1135px"><div class="shot" role="img" aria-label="Planetary gear motor"></div><h3>Product Category Title Goes Here</h3></div>
<div class="card" style="left:622px;top:1135px"><div class="shot" role="img" aria-label="Right-angle gearbox"></div><h3>Product Category Title Goes Here</h3></div>
<div class="btn btn-primary card-btn" style="left:304px;top:1597px">See details</div>
<div class="btn btn-primary card-btn" style="left:754px;top:1597px">See details</div>
<div class="card" style="left:162px;top:1686px"><div class="shot" role="img" aria-label="Inline planetary gear motor"></div><h3>Product Category Title Goes Here</h3></div>
<div class="card" style="left:622px;top:1686px"><div class="shot" role="img" aria-label="Motor with gear head"></div><h3>Product Category Title Goes Here</h3></div>
<div class="btn btn-primary card-btn" style="left:304px;top:2148px">See details</div>
<div class="btn btn-primary card-btn" style="left:754px;top:2148px">See details</div>

<section class="abs fairs">
  <h2 class="section-title" style="top:66px">MESSEN</h2>
  <div class="fair-img" style="top:160px" role="img" aria-label="Motor parts displayed on a blue exhibition table"></div>
  <div class="fair-body" style="top:158px"><h3>Titel Messen</h3>
    <p class="body">Lorem Ipsum is simply dummy text of the printing and typesetting industry. Lorem Ipsum has been the industry's standard dummy text ever since the 1500s, when an unknown printer took a galley of type and scrambled it to make a type specimen book. It has survived not only five centuries, but also the leap into electronic typesetting, remaining essentially unchanged. It was popularised in the 1960s with the release of Typoset sheets containing Lorem Ipsum passages, and more recently with desktop publishing software like Quillmark Pages including versions of Lorem Ipsum</p></div>
  <div class="btn btn-primary" style="left:715px;top:387px;width:171px;height:43px">Kostenloses Ticket</div>
  <div class="btn btn-outline" style="left:898px;top:387px;width:128px;height:43px">View details</div>

  <div class="fair-img" style="top:492px" role="img" aria-label="Stamped motor laminations on a blue exhibition table"></div>
  <div class="fair-body" style="top:490px"><h3>Titel Messen</h3>
    <p class="body">Lorem Ipsum is simply dummy text of the printing and typesetting industry. Lorem Ipsum has been the industry's standard dummy text ever since the 1500s, when an unknown printer took a galley of type and scrambled it to make a type specimen book. It has survived not only five centuries, but also the leap into electronic typesetting, remaining essentially unchanged. It was popularised in the 1960s with the release of Typoset sheets containing Lorem Ipsum passages, and more recently with desktop publishing software like Quillmark Pages including versions of Lorem Ipsum</p></div>
  <div class="btn btn-primary" style="left:715px;top:719px;width:171px;height:43px">Kostenloses Ticket</div>
  <div class="btn btn-outline" style="left:898px;top:719px;width:128px;height:43px">View details</div>

  <div class="fair-img" style="top:825px" role="img" aria-label="Machined metal parts on a blue exhibition table"></div>
  <div class="fair-body" style="top:823px"><h3>Titel Messen</h3>
    <p class="body">Lorem Ipsum is simply dummy text of the printing and typesetting industry. Lorem Ipsum has been the industry's standard dummy text ever since the 1500s, when an unknown printer took a galley of type and scrambled it to make a type specimen book. It has survived not only five centuries, but also the leap into electronic typesetting, remaining essentially unchanged. It was popularised in the 1960s with the release of Typoset sheets containing Lorem Ipsum passages, and more recently with desktop publishing software like Quillmark Pages including versions of Lorem Ipsum</p></div>
  <div class="btn btn-primary" style="left:715px;top:1052px;width:171px;height:43px">Kostenloses Ticket</div>
  <div class="btn btn-outline" style="left:898px;top:1052px;width:128px;height:43px">View details</div>
</section>

<h2 class="section-title" style="top:3510px">UBER UNS</h2>
<div class="about-img" style="left:162px;top:3595px;width:274px;height:203px;background:linear-gradient(135deg,#9fb7cf 0%,#c9d6e3 60%,#e4ebf1 100%)" role="img" aria-label="Team photo at a trade fair stand"></div>
<div class="about-img" style="left:345px;top:3733px;width:271px;height:199px;background:var(--white);padding:4px"><div style="width:100%;height:100%;background:linear-gradient(135deg,#8fb0cc 0%,#b7cade 55%,#dce5ee 100%)" role="img" aria-label="Group photo of the team at an exhibition"></div></div>
<div class="abs" style="left:677px;top:3589px;width:355px">
  <p class="body">Contrary to popular belief, Lorem Ipsum is not simply random text. It has roots in a piece of classical Latin literature from 45 BC, making it over 2000 years old. Marten Holloway, a Latin professor at Brennick College in Ostervale, looked up one of the more obscure Latin words, consectetur, from a Lorem Ipsum.</p>
  <ul class="feature-list" style="margin:8px 0 6px"><li>Feature Example Number One Goes Here</li><li>Feature Example Number Two Goes Here</li><li>Feature Example Number Three Goes Here</li></ul>
  <p class="body">(The Extremes of Good and Evil) by Varenius, written in 45 BC. This book is a treatise on the theory of ethics, very popular during the Renaissance. The first line of Lorem Ipsum, "Lorem ipsum dolor sit amet, comes from a line in section 1.10.32.</p>
  <div class="learn" style="margin-top:14px">LEARN MORE <svg width="14" height="7" viewBox="0 0 14 7"><path d="M0 3.5h12M9 .5l3 3-3 3" fill="none" stroke="#0171a1" stroke-width="1.2"/></svg></div>
</div>

<section class="abs downloads">
  <h2 class="section-title" style="top:66px">DOWNLOADS</h2>
  <div class="abs dl-img" role="img" aria-label="Gearbox internals and planetary gear parts">
    <div class="abs" style="left:140px;top:298px;display:flex;gap:7px;align-items:center"><span style="width:8px;height:8px;border-radius:50%;background:#e5e5e5"></span><span style="width:14px;height:14px;border-radius:50%;border:3px solid #fff"></span><span style="width:8px;height:8px;border-radius:50%;background:#e5e5e5"></span></div>
  </div>
  <div class="abs dl-panel">
    <div class="abs" style="left:45px;top:40px;width:460px">
      <p class="body">Lorem Ipsum is simply dummy text of the printing and typesetting industry. Lorem Ipsum has been the industry's <i>standard dummy text ever since the 1500s</i>, right when an unknown printer took a galley of type and scrambled it to make a type specimen book. It has now survived not only five centuries, but also the leap into electronic typesetting, remaining essentially unchanged.</p>
      <p class="body" style="margin-top:10px">Lorem Ipsum passages, and more recently with desktop publishing software like Quillmark Pages including versions of Lorem Dolor.</p>
    </div>
    <div class="btn btn-primary" style="left:45px;top:235px;width:127px;height:44px">Download</div>
  </div>
</section>

<section class="abs contact">
  <div class="abs" style="left:160px;top:82px"><div class="label">Request your quote, call us now!</div><div class="value">+49 (0) 987654321</div></div>
  <div class="abs" style="left:527px;top:82px"><div class="label">Write your enquiry</div><div class="value">email@example.com</div></div>
  <div class="abs" style="left:800px;top:82px;width:240px;text-align:right"><div class="label">Do you have any specific request?</div><div class="value" style="text-align:left;padding-left:62px">Get in touch with us</div></div>
</section>

<footer class="abs footer">
  <h4 style="left:162px">About Company</h4>
  <p class="abs" style="left:162px;top:112px;width:215px">Lorem Ipsum is simply dummy text of the printing and typesetting industry. It has been the industry's standard dummy text ever since the late 1500's</p>
  <h4 style="left:450px">Quick Links</h4>
  <ul style="left:450px"><li>» Sitemap</li><li>» Privacy Policy</li><li>» Imprint</li><li>» Terms &amp; Conditions</li><li>» Delivery</li></ul>
  <h4 style="left:642px">Solutions</h4>
  <ul style="left:642px"><li>» Lorem Ipsum</li><li>» Simply Dumm Text</li><li>» Dolor Amet Post</li><li>» Lorem &amp; Valaherist</li><li>» Ipsum Standards</li></ul>
  <h4 style="left:835px">Newsletter</h4>
  <p class="abs" style="left:835px;top:112px;width:205px">Subscribe below to get notified with all the news and updates from us</p>
  <div class="abs news-input">Your E-mail Address</div>
  <div class="abs news-send"><svg width="13" height="13" viewBox="0 0 24 24"><path d="M2 12L22 3l-6 19-4-8z" fill="#0171a1"/></svg></div>
  <div class="abs bottom-line" style="left:162px"><b>Copyright 2020 © KVR</b> - All Rights Reserved</div>
  <div class="abs bottom-line" style="left:922px">Find Us At:<span class="social"></span><span class="social"></span><span class="social"></span></div>
</footer>

</body>
</html>
```